Real Estate Sign - For Sale Yard Sign - Bellwether Estates

Our real estate company is looking for a new sign design to hang from in post in the front yard of the homes we are selling. Our company name is Bellwether Estates and we are open to any ideas. Attached for you is our company logo and name. The font is Trajan Pro. We are looking for a classy sign to put in front of our high end more expensive homes. You can either choose to include or not include the words "FOR SALE" on the sign (in our state, only about 1/2 of the real estate signs have room for those words. It is implied with a sign in the yard in front of a home). Thank you.

24 inches wide is important. and the height should be either 18, 24 or 30 inches. For printing purposes either of those heights will work. 18 inches is common, but some signs look great that are taller too. I'm open.

If you have any ideas for some better text options, styles or fonts, feel free to play with it.

P.S. Please feel free to play with the colors. We are not at this point set on a particular color scheme. Colors we think are nice but you may have other better ideas are black, red, white, gold, green

Target Market(s)

High end real estate home owners who choose to use our company to sell their home.

Industry/Entity Type

Real Estate

Requirements
Must have
• Company Logo
Company Name (Bellwether Estates)
Thaddeus Vornholt (please include my name as I am the real estate agent)
503-618-2940 (my phone number for potential clients to contact me)
Website name - bellwetherestatesnw.example
***You can either choose to include the words "FOR SALE" or not***

Dimensions must be 24 inches wide. Height can be either 18, 24 or 30 inches. Must be one of those 3 heights for printing purposes.

```html
<!DOCTYPE html>
<html lang="en">
<head>
<meta charset="utf-8">
<title>Bellwether Estates – For Sale Yard Sign Colour Options</title>
<link rel="stylesheet" href="https://fonts.googleapis.com/css2?family=Cinzel:wght@400;600&display=swap">
<style>
  :root {
    --red-light: #f0262c;
    --red-dark: #c0141a;
    --navy-light: #0d1596;
    --navy-dark: #02095a;
    --silver-light: #ececec;
    --silver-dark: #c6c6c6;
    --ink: #111111;
    --white: #ffffff;
    --page: #ffffff;
  }
  * { box-sizing: border-box; margin: 0; padding: 0; }
  html, body {
    width: 1200px; height: 848px; overflow: hidden;
    background: var(--page);
    font-family: "Cinzel", "Times New Roman", serif;
  }
  .sheet { position: relative; width: 1200px; height: 848px; }

  .sign {
    position: absolute; width: 420px; height: 291px;
    border-radius: 11px; overflow: hidden;
  }
  .sign--tl { left: 172px; top: 116px; }
  .sign--tr { left: 649px; top: 114px; }
  .sign--bl { left: 173px; top: 443px; }
  .sign--br { left: 650px; top: 443px; }

  .sign--red  { background: linear-gradient(180deg, var(--red-light), var(--red-dark)); }
  .sign--navy { background: linear-gradient(180deg, var(--navy-light), var(--navy-dark)); }

  .brand-panel {
    position: absolute; left: 10px; top: 10px; width: 400px; height: 184px;
    border-radius: 8px 8px 0 0;
    --panel-ink: var(--white); --panel-mark: var(--red-light);
  }
  .brand-panel--silver {
    background: linear-gradient(180deg, var(--silver-light), var(--silver-dark));
    --panel-ink: var(--ink); --panel-rule: var(--navy-light); --panel-ornament: var(--navy-light);
  }
  .brand-panel--navy {
    background: linear-gradient(180deg, var(--navy-light), var(--navy-dark));
    --panel-rule: var(--white); --panel-ornament: var(--white);
  }
  .brand-panel--red {
    background: linear-gradient(180deg, var(--red-light), var(--red-dark));
    --panel-rule: var(--white); --panel-ornament: var(--white); --panel-mark: var(--white);
  }

  .ornament {
    position: absolute; left: 110px; width: 180px; height: 22px;
    border-radius: 11px; background: var(--panel-ornament); opacity: 0.35;
  }
  .ornament--top { top: 10px; }
  .ornament--bottom { top: 150px; }

  .double-rule {
    position: absolute; left: 30px; width: 340px; height: 5px;
    border-top: 1.5px solid var(--panel-rule);
    border-bottom: 1.5px solid var(--panel-rule);
  }
  .double-rule--top { top: 34px; }
  .double-rule--bottom { top: 140px; }

  .brand {
    position: absolute; left: 0; top: 56px; width: 400px; height: 70px;
    display: flex; align-items: center; justify-content: center; gap: 10px;
  }
  .brand__dot {
    width: 18px; height: 18px; border-radius: 50%; background: var(--panel-mark);
    flex: none;
  }
  .brand__name {
    font-size: 23px; font-weight: 600; letter-spacing: 0.02em;
    color: var(--panel-ink); text-transform: uppercase; white-space: nowrap;
  }

  .listing {
    position: absolute; left: 0; top: 196px; width: 420px; height: 95px;
    color: var(--white); text-align: center;
  }
  .listing__status {
    font-size: 44px; font-weight: 400; line-height: 1; margin-top: 8px;
    letter-spacing: 0.01em;
  }
  .listing__agent {
    display: flex; justify-content: center; gap: 22px;
    font-size: 21px; margin-top: 8px; letter-spacing: 0.01em;
  }
</style>
</head>
<body>
<main class="sheet">

  <section class="sign sign--red sign--tl">
    <div class="brand-panel brand-panel--silver">
      <div class="ornament ornament--top" role="img" aria-label="Scrolling flourish ornament"></div>
      <div class="double-rule double-rule--top"></div>
      <div class="brand"><span class="brand__dot"></span><span class="brand__name">Bellwether Estates</span></div>
      <div class="double-rule double-rule--bottom"></div>
      <div class="ornament ornament--bottom" role="img" aria-label="Scrolling flourish ornament"></div>
    </div>
    <div class="listing">
      <p class="listing__status">FOR SALE</p>
      <p class="listing__agent"><span>Thaddeus Vornholt</span><span>503-618-2940</span></p>
    </div>
  </section>

  <section class="sign sign--red sign--tr">
    <div class="brand-panel brand-panel--navy">
      <div class="ornament ornament--top" role="img" aria-label="Scrolling flourish ornament"></div>
      <div class="double-rule double-rule--top"></div>
      <div class="brand"><span class="brand__dot"></span><span class="brand__name">Bellwether Estates</span></div>
      <div class="double-rule double-rule--bottom"></div>
      <div class="ornament ornament--bottom" role="img" aria-label="Scrolling flourish ornament"></div>
    </div>
    <div class="listing">
      <p class="listing__status">FOR SALE</p>
      <p class="listing__agent"><span>Thaddeus Vornholt</span><span>503-618-2940</span></p>
    </div>
  </section>

  <section class="sign sign--navy sign--bl">
    <div class="brand-panel brand-panel--silver">
      <div class="ornament ornament--top" role="img" aria-label="Scrolling flourish ornament"></div>
      <div class="double-rule double-rule--top"></div>
      <div class="brand"><span class="brand__dot"></span><span class="brand__name">Bellwether Estates</span></div>
      <div class="double-rule double-rule--bottom"></div>
      <div class="ornament ornament--bottom" role="img" aria-label="Scrolling flourish ornament"></div>
    </div>
    <div class="listing">
      <p class="listing__status">FOR SALE</p>
      <p class="listing__agent"><span>Thaddeus Vornholt</span><span>503-618-2940</span></p>
    </div>
  </section>

  <section class="sign sign--navy sign--br">
    <div class="brand-panel brand-panel--red">
      <div class="ornament ornament--top" role="img" aria-label="Scrolling flourish ornament"></div>
      <div class="double-rule double-rule--top"></div>
      <div class="brand"><span class="brand__dot"></span><span class="brand__name">Bellwether Estates</span></div>
      <div class="double-rule double-rule--bottom"></div>
      <div class="ornament ornament--bottom" role="img" aria-label="Scrolling flourish ornament"></div>
    </div>
    <div class="listing">
      <p class="listing__status">FOR SALE</p>
      <p class="listing__agent"><span>Thaddeus Vornholt</span><span>503-618-2940</span></p>
    </div>
  </section>

</main>
</body>
</html>
```